Duel Business card

Want an edgy business card that shows both of our companies on each side of the card, OR both together with a cool design.

*Must be edgy: We have attached our two business logos. We are a bail bond and immigration bond company.

Would like the address on one side only.
Need Phone, cell, website, address, and Name

Company Name 1: Cellgate Release Partners
www.cellgatereleasepartners.example

Company Name 2: Borderline Surety Associates
www.borderlinesuretyassociates.example

These cards will need to be easily changeable so I can modify new employees

Target Market(s)

people in jail, takign imigrants out of jail and from being taken back to there country

Industry/Entity Type

Business

Requirements
Must have
• Include both logos attached

```html
<!DOCTYPE html>
<html lang="en">
<head>
<meta charset="utf-8">
<title>Cellgate Release Partners &amp; Borderline Surety Associates — Business Card</title>
<link rel="stylesheet" href="https://fonts.googleapis.com/css2?family=Open+Sans:wght@400;700&display=swap">
<style>
  :root {
    --backdrop: #d9d9d9;
    --paper: #ffffff;
    --navy: #2f4a8e;
    --navy-deep: #1f3472;
    --red: #f2231c;
    --orange: #f2a31c;
    --ink: #1c2a5c;
    --card-shadow: 0 14px 30px rgba(0,0,0,.28);
  }
  * { box-sizing: border-box; margin: 0; padding: 0; }
  html, body { width: 1200px; height: 900px; overflow: hidden; }
  body {
    background: var(--backdrop);
    font-family: "Open Sans", Arial, sans-serif;
    position: relative;
  }
  .card {
    position: absolute;
    left: 250px;
    width: 700px;
    height: 400px;
    background: var(--paper);
    box-shadow: var(--card-shadow);
    overflow: hidden;
  }
  .card--details { top: 40px; }
  .card--brand { top: 470px; }
  .card__art { position: absolute; inset: 0; width: 100%; height: 100%; }

  .brand-mark {
    position: absolute;
    display: flex;
    align-items: center;
    gap: 10px;
    font-weight: 700;
    color: var(--ink);
    line-height: 1.1;
  }
  .brand-mark__dot {
    flex: none;
    border-radius: 50%;
    background: var(--navy);
  }
  .card--details .brand-mark { font-size: 17px; }
  .card--details .brand-mark__dot { width: 56px; height: 56px; }
  .card--details .brand-mark--surety { left: 28px; top: 22px; width: 200px; }
  .card--details .brand-mark--release { left: 250px; top: 30px; width: 230px; }
  .card--details .brand-mark--release .brand-mark__dot { width: 40px; height: 40px; }

  .contact {
    position: absolute;
    left: 28px;
    top: 210px;
    color: var(--paper);
    font-size: 21px;
    line-height: 1.33;
    list-style: none;
  }

  .card--brand .brand-mark { font-size: 26px; }
  .card--brand .brand-mark--surety { left: 150px; top: 26px; width: 300px; }
  .card--brand .brand-mark--surety .brand-mark__dot { width: 70px; height: 70px; }
  .card--brand .brand-mark--release { left: 60px; top: 170px; width: 330px; }
  .card--brand .brand-mark--release .brand-mark__dot { width: 56px; height: 56px; }
</style>
</head>
<body>

<section class="card card--details">
  <svg class="card__art" viewBox="0 0 700 400" preserveAspectRatio="none" aria-hidden="true">
    <path d="M0 200 C 180 175, 420 150, 700 105 L700 400 L0 400 Z" fill="var(--navy)"/>
    <path d="M190 166 C 330 150, 470 130, 620 108 C 470 140, 330 158, 190 172 Z" fill="var(--navy-deep)"/>
  </svg>
  <div class="brand-mark brand-mark--surety">
    <span class="brand-mark__dot"></span>
    <span>Borderline Surety Associates</span>
  </div>
  <div class="brand-mark brand-mark--release">
    <span class="brand-mark__dot"></span>
    <span>Cellgate Release Partners</span>
  </div>
  <ul class="contact">
    <li>Cellgate Release Partners and Borderline Surety Associates</li>
    <li>P: 555-555-5555 &bull; M: 555-555-5555</li>
    <li>Web: www.cellgatereleasepartners.example</li>
    <li>Web: www.borderlinesuretyassociates.example</li>
    <li>214 Harbor Row Street, City, XX, 555555</li>
  </ul>
</section>

<section class="card card--brand">
  <svg class="card__art" viewBox="0 0 700 400" preserveAspectRatio="none" aria-hidden="true">
    <path d="M330 0 C 520 60, 520 300, 360 400 L700 400 L700 0 Z" fill="var(--red)"/>
    <path d="M300 0 C 500 70, 500 300, 330 400" fill="none" stroke="var(--navy)" stroke-width="2"/>
    <path d="M318 0 C 512 66, 512 300, 346 400" fill="none" stroke="var(--orange)" stroke-width="2"/>
    <path d="M326 4 C 515 70, 515 296, 352 400" fill="none" stroke="var(--orange)" stroke-width="1.5"/>
  </svg>
  <div class="brand-mark brand-mark--surety">
    <span class="brand-mark__dot"></span>
    <span>Borderline Surety Associates</span>
  </div>
  <div class="brand-mark brand-mark--release">
    <span class="brand-mark__dot"></span>
    <span>Cellgate Release Partners</span>
  </div>
</section>

</body>
</html>
```